Design Real Estate Banking Comparison - between 3 different types of lenders

We need a design to add to a page of our website. We want the design to paint a picture for the user to help them understand who we are, as opposed to writing a long paragraph. We consider ourselves a unique Real Estate Lender. We are not a Hard Money lender and we are not a Institutional (Bank) Lender. We are right in the middle. We want to show people that we are different then the other two choices. We have had the idea of showing us in the middle represented by something like a vintage lightbulb (we are certainly open to other suggestions.) Off to the distance in the left could be a large bank with people waiting out front with shackles on their feet as they try to get approved for a loan, or something that represents how it’s difficult to work with large banks. Off to the distance to the right could be a hard money lender with money being squeezed and blood coming out as they take advantage of their borrowers. Something that shows them as being greedy.
We are not expensive like a hard money lender, and we are much more accommodating then a bank. We want to show this through a design..
Our company name is Harbor Ridge Lending so we like to keep our brand and material 'Harbor" yet very transitional too, to appeal to the younger and more sophisticated internet user.
I'll attached a screen shot of our website so you can see our colors and look.

Target Market(s)

Real Estate - Real Estate Investments - Real Estate Lending

Industry/Entity Type

Real Estate

Number of Pages Required

1 page

Requirements
Must have
• Colors - Please see our company Logo in the attachment
Nice to have
• See description - Please know we are open to other ideas as well that will be able to "paint the picture" we are trying to get across to the user.

```html
<!DOCTYPE html>
<html lang="en">
<head>
<meta charset="utf-8">
<title>Harbor Ridge Lending – What We Do</title>
<link rel="stylesheet" href="https://fonts.googleapis.com/css2?family=Cinzel:wght@400;700&family=Lato:wght@400;700&display=swap">
<style>
  :root {
    --gold: #e0b856;
    --gold-deep: #c99a35;
    --ink: #2b2b2b;
    --charcoal: #333333;
    --black: #0d0d0d;
    --cream: #fdf9ec;
    --cream-band: #faf6ea;
    --grey: #9a9a9a;
    --grey-light: #d3d3d3;
    --white: #ffffff;
  }
  * { margin: 0; padding: 0; box-sizing: border-box; }
  html, body { width: 1200px; height: 2230px; overflow: hidden; }
  body { position: relative; background: var(--white); font-family: "Lato", sans-serif; color: var(--ink); }
  .abs { position: absolute; }

  /* Header */
  .site-header { position: absolute; left: 0; top: 0; width: 1200px; height: 80px; background: var(--charcoal); }
  .brand { position: absolute; left: 80px; top: 24px; font-family: "Cinzel", serif; font-size: 27px; color: var(--gold); letter-spacing: 1px; }
  .main-nav { position: absolute; right: 78px; top: 30px; display: flex; gap: 32px; font-size: 14px; color: var(--white); letter-spacing: .3px; }
  .main-nav .active { border-bottom: 2px solid var(--gold); padding-bottom: 6px; }

  /* Hero */
  .hero { position: absolute; left: 0; top: 80px; width: 1200px; height: 286px;
    background: linear-gradient(180deg, #6e5a3c 0%, #8a7350 45%, #5e4c33 100%); }
  .hero-title { position: absolute; left: 0; top: 168px; width: 1200px; text-align: center; font-family: "Cinzel", serif; font-size: 72px; color: var(--white); letter-spacing: 2px; }

  /* Intro */
  .intro { position: absolute; left: 0; top: 366px; width: 1200px; height: 252px; background: var(--cream); text-align: center; }
  .intro-lead { margin-top: 46px; font-size: 21px; font-weight: 700; }
  .intro-text { width: 1030px; margin: 6px auto 0; font-size: 18.5px; line-height: 31px; }

  /* Values */
  .values-title { position: absolute; top: 660px; font-family: "Cinzel", serif; font-size: 50px; color: var(--ink); }
  .value { position: absolute; top: 778px; width: 250px; text-align: center; }
  .value h3 { font-family: "Cinzel", serif; font-weight: 700; font-size: 20px; letter-spacing: 1px; margin-bottom: 4px; }
  .value p { font-size: 13.5px; line-height: 22.5px; }

  /* Comparison */
  .lender { position: absolute; text-align: center; }
  .lender h3 { font-family: "Cinzel", serif; font-weight: 400; font-size: 24px; letter-spacing: 1px; margin-bottom: 8px; }
  .lender p { font-size: 14px; line-height: 23px; }
  .lender.featured h3 { font-weight: 700; font-size: 26px; }
  .lender.featured p { font-size: 16px; line-height: 27px; }

  /* Performance */
  .performance { position: absolute; left: 0; top: 1393px; width: 1200px; height: 540px; background: var(--cream-band); }
  .year { position: absolute; top: 410px; font-size: 21px; color: var(--grey); transform: translateX(-50%); }
  .stat { position: absolute; width: 130px; height: 130px; border-radius: 50%; background: var(--white); text-align: center; box-shadow: 0 2px 8px rgba(0,0,0,.05); }
  .stat .label { margin-top: 30px; font-size: 14px; font-weight: 700; }
  .stat .value-num { font-size: 27px; font-weight: 700; line-height: 30px; }
  .stat .sub { font-size: 14px; color: var(--grey); }
  .stat.gold .label { color: var(--gold); }
  .stat .value-num, .stat.grey .label { color: var(--grey); }
  .caption { position: absolute; left: 167px; top: 468px; font-size: 14.5px; color: var(--grey); }

  /* Call to action */
  .cta-title { position: absolute; left: 0; top: 1972px; width: 1200px; text-align: center; font-family: "Cinzel", serif; font-weight: 700; font-size: 42px; color: var(--ink); letter-spacing: 1px; }
  .cta-button { position: absolute; left: 464px; top: 2045px; width: 272px; height: 62px; background: var(--gold); color: var(--white); font-size: 30px; line-height: 62px; text-align: center; }

  /* Footer */
  .footer-contact { position: absolute; left: 0; top: 2160px; width: 1200px; height: 32px; background: var(--charcoal); color: var(--white); font-size: 14px; line-height: 32px; text-align: center; }
  .footer-legal { position: absolute; left: 0; top: 2192px; width: 1200px; height: 38px; background: var(--black); color: var(--white); font-size: 13px; line-height: 38px; text-align: center; }
</style>
</head>
<body>

<header class="site-header">
  <div class="brand">HARBOR RIDGE LENDING</div>
  <nav class="main-nav">
    <span>HOME</span><span class="active">WHY HARBOR</span><span>BORROW</span><span>INVEST</span><span>PORTFOLIO</span><span>CONTACT US</span>
  </nav>
</header>

<section class="hero" role="img" aria-label="Sepia photograph of a stone bridge tower with gothic arches and suspension cables"></section>
<h1 class="hero-title">What&nbsp; We Do ?</h1>

<section class="intro">
  <p class="intro-lead">Harbor Ridge Lending is a professional real estate lending and investment company.</p>
  <p class="intro-text">We provide capital for acquisition, development, reposition, value add, and strategic purchases throughout the United States. A combination of proven experience and a broad and balanced base of capital partners enables Harbor to provide reliable financing in a rapid and efficient manner. Our focus is to provide individualized, fair and flexible funding that empowers borrowers and development partners.</p>
</section>

<div class="values-title" style="left:108px">Real Results</div>
<div class="values-title" style="left:478px">Real People</div>
<div class="values-title" style="left:820px">Authentic</div>

<svg class="abs" style="left:0;top:690px" width="1200" height="72" aria-hidden="true">
  <g stroke="#2b2b2b" stroke-width="1.3" fill="none">
    <path d="M78 4 V38 H1122 V4"/>
    <line x1="188" y1="38" x2="188" y2="64"/>
    <line x1="453" y1="38" x2="453" y2="64"/>
    <line x1="727" y1="38" x2="727" y2="64"/>
    <line x1="1013" y1="38" x2="1013" y2="64"/>
  </g>
  <g fill="#2b2b2b">
    <circle cx="188" cy="65" r="4.5"/><circle cx="453" cy="65" r="4.5"/>
    <circle cx="727" cy="65" r="4.5"/><circle cx="1013" cy="65" r="4.5"/>
  </g>
</svg>

<div class="value" style="left:63px"><h3>Flexible</h3><p>Unlike typical hard money lenders, we seek to provide options to each individual borrower, such as low introductory rates, low cost extensions, discounts to repeat borrowers, and more.</p></div>
<div class="value" style="left:328px"><h3>Experienced</h3><p>We are a group of experienced real estate professionals providing innovate capital solutions for all residential and commercial needs.</p></div>
<div class="value" style="left:602px"><h3>Reliable</h3><p>We focus on the individual and work to build long-term relationships and meet the needs of repeat borrowers. We accomplish this by being accessible and highly responsive to the needs of both our borrowers and investors.</p></div>
<div class="value" style="left:888px"><h3>Transparent</h3><p>We have your best interest in mind. We have a transparent structure that includes an annual audit, an experienced board of advisors, and a reputable third party fund administrator.</p></div>

<!-- Balance scale -->
<svg class="abs" style="left:440px;top:1010px" width="320" height="140" aria-hidden="true">
  <g fill="none" stroke="#e0b856" stroke-width="8">
    <circle cx="63" cy="58" r="42"/>
    <circle cx="247" cy="58" r="42"/>
  </g>
  <g fill="#e0b856">
    <circle cx="63" cy="24" r="4"/><circle cx="63" cy="92" r="4"/><circle cx="29" cy="58" r="4"/><circle cx="97" cy="58" r="4"/>
  </g>
  <path d="M63 58 L40 48 M63 58 L78 40" stroke="#e0b856" stroke-width="7" stroke-linecap="round"/>
  <text x="247" y="75" text-anchor="middle" font-family="Lato, sans-serif" font-weight="700" font-size="48" fill="#e0b856">$</text>
  <rect x="16" y="119" width="278" height="9" rx="4.5" fill="#e0b856"/>
</svg>

<!-- Bank icon -->
<svg class="abs" style="left:180px;top:1102px" width="100" height="100" aria-hidden="true">
  <circle cx="50" cy="50" r="44" fill="none" stroke="#2b2b2b" stroke-width="8"/>
  <text x="50" y="68" text-anchor="middle" font-family="Lato, sans-serif" font-weight="700" font-size="50" fill="#2b2b2b">$</text>
</svg>

<!-- Hard money clock icon -->
<svg class="abs" style="left:918px;top:1102px" width="100" height="100" aria-hidden="true">
  <circle cx="50" cy="50" r="44" fill="none" stroke="#2b2b2b" stroke-width="8"/>
  <g fill="#2b2b2b"><circle cx="50" cy="16" r="4"/><circle cx="50" cy="84" r="4"/><circle cx="16" cy="50" r="4"/><circle cx="84" cy="50" r="4"/></g>
  <path d="M50 50 L28 40 M50 50 L66 32" stroke="#2b2b2b" stroke-width="7" stroke-linecap="round"/>
</svg>

<div class="lender" style="left:70px;top:1220px;width:320px"><h3>Bank</h3><p>While banks rates are lower then your typical hard money lender, they have stringent guidelines, lengthy turn times and lack flexibility</p></div>
<div class="lender featured" style="left:440px;top:1208px;width:320px"><h3>Harbor Ridge Lending</h3><p>Your perfect solution. More accommodating then a Bank and less expensive then a Hard Money Lender</p></div>
<div class="lender" style="left:808px;top:1220px;width:320px"><h3>Hard Money Lender</h3><p>Generally more lenient guidelines, quicker turn times and more accommodating then banks, but you can expect higher rates and expensive fees</p></div>

<section class="performance">
  <svg class="abs" style="left:109px;top:47px" width="830" height="350" aria-label="Growth chart: real estate versus stock index, 2000 to 2016" role="img">
    <defs>
      <linearGradient id="areaFill" x1="0" y1="0" x2="0" y2="1">
        <stop offset="0" stop-color="#e0b856" stop-opacity=".55"/>
        <stop offset="1" stop-color="#e0b856" stop-opacity="0"/>
      </linearGradient>
    </defs>
    <g stroke="#ece6d6" stroke-width="1">
      <line x1="0" y1="0" x2="0" y2="345"/><line x1="103" y1="0" x2="103" y2="345"/><line x1="206" y1="0" x2="206" y2="345"/>
      <line x1="309" y1="0" x2="309" y2="345"/><line x1="412" y1="0" x2="412" y2="345"/><line x1="516" y1="0" x2="516" y2="345"/>
      <line x1="619" y1="0" x2="619" y2="345"/><line x1="722" y1="0" x2="722" y2="345"/><line x1="825" y1="0" x2="825" y2="345"/>
    </g>
    <path fill="url(#areaFill)" d="M0 292 L26 290 L52 282 L80 278 L103 270 L130 265 L155 258 L180 246 L206 230 L232 215 L258 203 L280 185 L310 166 L335 140 L361 95 L375 105 L395 130 L410 128 L428 140 L440 158 L452 225 L460 250 L468 240 L480 200 L500 185 L516 172 L540 150 L560 120 L575 132 L600 118 L610 150 L630 140 L650 120 L670 96 L690 78 L710 70 L722 45 L740 40 L760 20 L780 35 L800 45 L825 30 L825 345 L0 345 Z"/>
    <path fill="none" stroke="#e0b856" stroke-width="4" stroke-linejoin="round" d="M0 292 L26 290 L52 282 L80 278 L103 270 L130 265 L155 258 L180 246 L206 230 L232 215 L258 203 L280 185 L310 166 L335 140 L361 95 L375 105 L395 130 L410 128 L428 140 L440 158 L452 225 L460 250 L468 240 L480 200 L500 185 L516 172 L540 150 L560 120 L575 132 L600 118 L610 150 L630 140 L650 120 L670 96 L690 78 L710 70 L722 45 L740 40 L760 20 L780 35 L800 45 L825 30"/>
    <circle cx="825" cy="30" r="6" fill="#e0b856"/>
    <path fill="none" stroke="#d3d3d3" stroke-width="3.5" stroke-linejoin="round" d="M0 292 L40 298 L80 305 L120 302 L160 308 L206 300 L258 298 L309 292 L361 288 L400 296 L440 300 L460 318 L480 322 L516 310 L560 306 L600 302 L640 290 L690 280 L722 272 L760 268 L800 272 L825 267"/>
    <circle cx="825" cy="267" r="6" fill="#d3d3d3"/>
  </svg>
  <span class="year" style="left:109px">2000</span><span class="year" style="left:212px">2002</span>
  <span class="year" style="left:315px">2004</span><span class="year" style="left:418px">2006</span>
  <span class="year" style="left:521px">2008</span><span class="year" style="left:625px">2010</span>
  <span class="year" style="left:728px">2012</span><span class="year" style="left:831px">2014</span>
  <span class="year" style="left:934px">2016</span>
  <div class="stat gold" style="left:985px;top:88px"><div class="label">Real Estate</div><div class="value-num">482%</div><div class="sub">Growth</div></div>
  <div class="stat grey" style="left:985px;top:249px"><div class="label">Stock Index</div><div class="value-num">80%</div><div class="sub">Growth</div></div>
  <p class="caption">Lorem ipsum dolor sit amet, consectetuer adipiscing elit, sed diam nonummy nibh euismod tincidunt</p>
</section>

<h2 class="cta-title">The future of real estate investing is here</h2>
<div class="cta-button">GET STARTED</div>

<footer>
  <div class="footer-contact">120 Bayview Ave. Suite 300 | Clearwater CA 90210 | (555) 201-4470 | hello@harborridgelend.com</div>
  <div class="footer-legal">Harbor Ridge Lending 2016.</div>
</footer>

</body>
</html>
```